Professional, polished website design for boutique wealth management firm

Hello, thank you for your interest. PLEASE READ THE BRIEF BEFORE SUBMITTING THE DESIGN.-
PLEASE USE THE ATTACHED HOME PAGE COPY FOR THIS DESIGN.
We are looking for a professional, polished design that helps portray trust and credibility for a well-established independent wealth management firm. We have copy we've written for the home page and we'd like the design and imagery to play up the copy, so there's a better chance someone will read it all. So the headlines etc should all be easy to read and the design should draw the eye towards them. For colors, again trust is important so probably blue as a dominant color, but you can also use gray, green, etc. We'd like to avoid too much use of the color red (due to financial, association with loss). SO PLEASE AVOID USE OF THE COLOR RED. We also like bright orange or yellow for call to action buttons.

Please keep the design EASY TO MAINTAIN in wordpress as well.

I have attached home page copy as well as logo files.

Here's some sites that we like so feel free to use as inspiration:
https://www.brovaltcapitalworks.example/, https://harborpathpensionsplains.example/
https://tavrin-oakes.example/, https://plantfornextyear.example/, https://ferngatefinancial.example/

As another option/idea, I like the idea of a simple format with a clean image similar to this for the home page: https://www.pixmeadowstock.example/detail/photo/calculator-falling-royalty-free-image/31684207?adppopup=true
Just an idea.

Also please be sure to incorporate the QWA /Accredited Wealth Steward logo as well, farther down the page is fine.

Thank you for your help! Feel free to contact me with any questions.

Target Market(s)

Individuals aged 48-62 who are looking to maximize their wealth, such as business owners, executives, engineers, successful tradespeople, etc.

Industry/Entity Type

Finance--wealth management

Font styles to use
Sans Serif

Requirements
Must have
• Professional and polished, Call to action buttons must be clear and stand out, headlines must be clear and stand out, also text must be big enough to be easily readable by most people
Should not have
• Anything casual, frilly, etc.

```html
<!DOCTYPE html>
<html lang="en">
<head>
<meta charset="utf-8">
<title>Harbrook Asset Advisors — Home</title>
<link href="https://fonts.googleapis.com/css2?family=Poppins:wght@300;400;500;600&display=swap" rel="stylesheet">
<style>
:root{
  --ink:#111111;
  --purple:#33309a;
  --lavender:#b9b6ff;
  --orange:#ff6a00;
  --navy-line:#1f3f8f;
  --navy:#0d2f63;
  --muted:#8a8a8a;
  --white:#ffffff;
  --head:'Poppins', Arial, sans-serif;
  --sans:'Poppins', Arial, sans-serif;
}
*{box-sizing:border-box;margin:0;padding:0}
html,body{width:1200px;height:3793px;overflow:hidden;background:var(--white)}
body{position:relative;font-family:var(--sans);color:var(--ink)}
.abs{position:absolute}
.btn{position:absolute;background:var(--orange);color:var(--white);font:500 13px/1 var(--sans);border-radius:6px;display:flex;align-items:center;justify-content:center;text-transform:uppercase;letter-spacing:.2px}
.dash-title{position:absolute;font:600 27px/1.38 var(--head);color:var(--ink)}
.dash-title::before{content:"";position:absolute;left:-52px;top:19px;width:38px;height:3px;background:var(--navy-line)}
.photo{position:absolute}

/* hero */
.hero{left:0;top:0;width:1200px;height:655px;border-radius:0 0 170px 170px;background:linear-gradient(100deg,#1d1d20 0%,#2e2e33 45%,#4a4642 75%,#2a2724 100%);border-bottom:3px solid var(--lavender);overflow:hidden}
.brand{position:absolute;display:flex;align-items:center;gap:8px;font:600 15px/1 var(--head);color:var(--white)}
.brand .dot{width:26px;height:26px;border-radius:50%;background:var(--navy-line)}
.nav{position:absolute;left:312px;top:28px;display:flex;gap:30px;font:400 13.5px/1 var(--sans);color:var(--white)}
.nav-cta{left:1005px;top:18px;width:135px;height:37px}
.hero h1{position:absolute;left:62px;top:180px;font:600 54px/1.25 var(--head);color:var(--white)}
.hero p{position:absolute;left:62px;top:348px;width:460px;font:400 17px/1.55 var(--sans);color:var(--white)}

/* strategies */
.intro-note{left:780px;top:752px;width:302px;text-align:right;font:400 13.5px/1.5 var(--sans);color:#555}
.card{position:absolute;top:873px;width:300px;height:375px;background:#050505;color:var(--white);padding:28px 31px}
.card .icon{width:64px;height:64px;border-radius:6px;background:linear-gradient(135deg,#6d6af0,#3f3ca8);margin-bottom:30px}
.card h3{font:600 16px/1.3 var(--head);margin-bottom:14px}
.card p{font:400 11.6px/1.62 var(--sans)}
.card-backdrop{left:424px;top:964px;width:275px;height:321px;background:linear-gradient(90deg,var(--purple),var(--lavender));border-radius:0 0 150px 0}

.text-block{position:absolute;font:400 12.5px/1.6 var(--sans);color:var(--muted)}

/* check-up */
.band{left:0;top:1883px;width:955px;height:450px;background:var(--purple);border-radius:0 110px 110px 0}
.band h2{position:absolute;left:155px;top:100px;font:600 27px/1.38 var(--head);color:var(--white)}
.band .rule{position:absolute;left:58px;top:119px;width:62px;height:3px;background:var(--orange)}
.band p{position:absolute;left:155px;top:195px;width:355px;font:400 12.3px/1.6 var(--sans);color:var(--white)}

/* services */
.swatches{left:1002px;top:2408px;display:flex}
.swatches span{width:37.5px;height:37px}
.svc-label{position:absolute;text-align:center;font:600 16px/1.55 var(--head);color:var(--ink)}

/* footer */
.footer{left:0;top:3349px;width:1200px;height:444px;background:linear-gradient(100deg,#121214,#242428 60%,#141416);border-radius:150px 150px 0 0;border-top:3px solid var(--lavender);overflow:hidden}
.footer h4{position:absolute;font:600 16px/1 var(--head);color:var(--white)}
.footer h4::before{content:"";position:absolute;left:-32px;top:9px;width:22px;height:2px;background:var(--orange)}
.footer .copy{position:absolute;font:400 12.5px/1.6 var(--sans);color:#e6e6e6}
.sitemap{list-style:none}
.sitemap li{margin-bottom:7px}
.contact-row{position:absolute;left:888px;display:flex;gap:14px;align-items:flex-start;font:400 12.5px/1.5 var(--sans);color:var(--white)}
.legal{position:absolute;left:0;bottom:0;width:1200px;height:38px;background:linear-gradient(90deg,var(--purple),#7b78e0 55%,var(--lavender));display:flex;align-items:center;justify-content:center;font:400 12.5px/1 var(--sans);color:#111}
</style>
</head>
<body>

<header class="abs hero">
  <div class="photo" role="img" aria-label="Woman reviewing financial documents and invoices at a desk with a calculator" style="left:520px;top:0;width:680px;height:655px;background:radial-gradient(ellipse at 60% 40%,rgba(150,135,120,.45),rgba(0,0,0,0) 70%)"></div>
  <div class="brand" style="left:60px;top:48px"><span class="dot"></span>HARBROOK</div>
  <nav class="nav"><span>Home</span><span>Why We Are ?</span><span>Better Strategies</span><span>Personalized Solutions</span><span>Retirement Check-Up</span></nav>
  <div class="btn nav-cta">Contact Us</div>
  <h1>Financial plans start<br>with tax planning.</h1>
  <p>Few financial advisors offer tax expertise, but<br>when they do, you benefit.</p>
  <div class="btn" style="left:60px;top:420px;width:135px;height:37px">Contact Us</div>
</header>

<h2 class="dash-title" style="left:110px;top:733px;width:570px">Better strategies to preserve and grow wealth, generate income and reduce your taxes</h2>
<p class="abs intro-note">Here's what you can expect when you work with Harbrook.</p>

<div class="abs card-backdrop"></div>
<article class="card" style="left:109px">
  <div class="icon" role="img" aria-label="Approach icon"></div>
  <h3>A Better Approach</h3>
  <p>Taxes are critical to every financial move you make, so we incorporate tax planning in everything we do for you. Along with managing your investments, we help you safely generate retirement income, reduce capital gains and minimize income taxes. We'll also help you with estate planning strategies so you can protect your family's future and make the most of opportunities.</p>
</article>
<article class="card" style="left:461px;background:linear-gradient(160deg,#1a1a1a,#050505)">
  <div class="icon" role="img" aria-label="Experience icon"></div>
  <h3>More Experience</h3>
  <p>You've worked hard to get where you are, so your money shouldn't have to be part of anyone's learning curve. At Harbrook Asset Advisors, you'll only work with seasoned experts, each with decades of investment, planning or tax experience. Our team works together to help solve your financial challenges and get your money working harder for you.</p>
</article>
<article class="card" style="left:791px">
  <div class="icon" role="img" aria-label="Fiduciary icon"></div>
  <h3>On Your Side</h3>
  <p>In an industry rife with conflicts of interest, you need a firm that works in your best interest. As an independent firm, we have no ties to insurance or mutual fund companies. We're fee-based, meaning we're compensated by fees, not commissions. We also act as your fiduciary, so we're ethically bound to put your interests first. That way, you get our best advice…not product recommendations.</p>
</article>

<div class="photo" role="img" aria-label="Hands using a calculator with a pen" style="left:121px;top:1387px;width:337px;height:368px;border-radius:14px;background:linear-gradient(135deg,#e8edf3,#9fb0c4 55%,#5c6c80)"></div>
<div class="photo" role="img" aria-label="Portrait of a smiling financial specialist" style="left:350px;top:1598px;width:206px;height:206px;border-radius:50%;border:5px solid #f4f4f7;background:linear-gradient(160deg,#4a6fb0,#1d2f5a)"></div>
<h2 class="dash-title" style="left:620px;top:1388px;width:480px">Cookie-cutter financial planning and investment can leave your future at risk. That's why we do it differently.</h2>
<p class="text-block" style="left:620px;top:1557px;width:340px">You need better strategies in today's complex financial landscape. At Harbrook Asset Advisors, we bring financial planning, investment management, retirement income, tax and estate planning expertise together under one roof. Our unique team works together to help you make the most of your resources.</p>
<div class="btn" style="left:619px;top:1700px;width:184px;height:37px">Meet Our Specialist</div>

<section class="abs band">
  <span class="rule"></span>
  <h2>The Harbrook $549<br>Retirement Check-Up</h2>
  <p>We know it's a big decision to hire or switch advisors. That's why we provide an easy way to try us out. At the same time, you can get a valuable second opinion to find out if you're on track to retire. There's no pressure, and either way, you'll walk away with valuable insights on what you should be doing to secure your future.</p>
  <div class="btn" style="left:154px;top:342px;width:142px;height:36px">Leran More</div>
  <div class="photo" role="img" aria-label="Advisors meeting with clients around a conference table" style="left:562px;top:67px;width:346px;height:330px;border-radius:22px;background:linear-gradient(150deg,#a48a74,#d8ccbf 45%,#7a746e)"></div>
</section>

<h2 class="dash-title" style="left:397px;top:2407px;width:540px">The most effective financial plans start with tax planning.</h2>
<div class="abs swatches"><span style="background:#c9c9c9"></span><span style="background:#c8c6ff"></span><span style="background:#ff6a00"></span><span style="background:#0d2f63"></span><span style="background:#00cfff"></span></div>

<div class="photo" role="img" aria-label="Hands reviewing investment charts with a phone" style="left:121px;top:2541px;width:208px;height:247px;border-radius:0 0 60px 0;background:linear-gradient(150deg,#3a3f4a,#c9ccd2 60%,#eceef2)"></div>
<p class="svc-label" style="left:111px;top:2808px;width:228px">Investment<br>Management</p>

<p class="svc-label" style="left:355px;top:2512px;width:225px">Comprehensive<br>Financial Planning</p>
<div class="abs" style="left:359px;top:2585px;width:216px;height:248px;border-radius:70px 0 0 0;background:var(--purple)"></div>
<div class="photo" role="img" aria-label="Two colleagues discussing a plan at a laptop" style="left:367px;top:2585px;width:208px;height:248px;border-radius:70px 0 0 0;background:linear-gradient(150deg,#8c9aa3,#3f6c5a 55%,#c3c8c4)"></div>

<div class="photo" role="img" aria-label="Person using a calculator over paperwork" style="left:612px;top:2541px;width:208px;height:247px;border-radius:0 0 0 60px;background:linear-gradient(150deg,#cfc8c2,#8d8580 50%,#3f3b39)"></div>
<p class="svc-label" style="left:605px;top:2808px;width:236px">Retirement Income<br>Planning</p>

<p class="svc-label" style="left:856px;top:2512px;width:228px">Tax Planning</p>
<div class="photo" role="img" aria-label="Close-up of blue calculator keys with a pen" style="left:866px;top:2578px;width:208px;height:248px;border-radius:0 60px 0 0;background:linear-gradient(150deg,#6fa0e0,#1e4ea8 55%,#0e2c6a)"></div>

<div class="photo" role="img" aria-label="Smiling advisor in shirt and tie holding a calculator and pointing" style="left:74px;top:2900px;width:471px;height:449px;border-radius:200px 200px 0 0;background:linear-gradient(180deg,#e9eef6 0%,#8fb1e3 40%,#4c78bd 100%)"></div>
<h2 class="dash-title" style="left:639px;top:2956px;width:540px">The most effective financial plans start with tax planning.</h2>
<p class="text-block" style="left:639px;top:3042px;width:440px;color:#666">Few financial advisors offer tax expertise, but when they do, you benefit. Learn how our unique team combines financial planning, investments and smart tax and income generation strategies to help you achieve your goals faster.</p>
<div class="btn" style="left:638px;top:3146px;width:183px;height:37px">Why We Diffrent</div>

<footer class="abs footer">
  <div class="brand" style="left:60px;top:110px"><span class="dot"></span>HARBROOK</div>

  <h4 style="left:368px;top:85px">About Us</h4>
  <p class="copy" style="left:337px;top:118px;width:232px">With over 55 years of combined experience, Harbrook Asset Advisors helps successful people more effectively prepare for the future. Our unique small team of wealth managers, financial planners and tax professionals bring you the strategies you need to preserve your wealth, minimize your taxes and create a confident retirement. While we're based in Ashby County, Ohio, we serve clients nationwide.</p>

  <h4 style="left:644px;top:85px">Site Map</h4>
  <ul class="copy sitemap" style="left:612px;top:118px">
    <li>- Home</li><li>- About us</li><li>- Better Setisfaction</li><li>- Personalized solutions</li><li>- Retirement</li><li>- Contact Us</li>
  </ul>

  <h4 style="left:920px;top:85px">Contact Us</h4>
  <div class="contact-row" style="top:115px">
    <svg width="18" height="22" viewBox="0 0 18 22" aria-hidden="true"><path d="M9 1a7 7 0 0 0-7 7c0 5 7 13 7 13s7-8 7-13a7 7 0 0 0-7-7z" fill="none" stroke="#7b78e0" stroke-width="2"/><circle cx="9" cy="8" r="2.5" fill="#7b78e0"/></svg>
    <span>Lorem ipsum is dummy text<br>printing industry.</span>
  </div>
  <div class="contact-row" style="top:176px">
    <svg width="18" height="14" viewBox="0 0 18 14" aria-hidden="true"><rect x="1" y="1" width="16" height="12" fill="none" stroke="#7b78e0" stroke-width="2"/><path d="M1 1l8 7 8-7" fill="none" stroke="#7b78e0" stroke-width="2"/></svg>
    <span>info@harbrook.example</span>
  </div>
  <div class="contact-row" style="top:216px">
    <svg width="18" height="18" viewBox="0 0 18 18" aria-hidden="true"><path d="M4 1l3 4-2 2c1 3 3 5 6 6l2-2 4 3-2 3C8 17 1 10 1 3z" fill="#7b78e0"/></svg>
    <span>123 456 7890</span>
  </div>

  <div class="legal">Copyright © 2021 HARBROOK- All Right Resrved.</div>
</footer>

</body>
</html>
```